Lumvex Crating Business Card

Project Overview
We are seeking a modern, minimalist business card that effectively represents our company while making a bold and lasting impression. The design should reflect trust, professionalism, and innovation, reinforcing our expertise in custom plastic manufacturing for warehouse and distribution centers.

Provided Assets & Specifications
Logo: We will provide our official logo for integration into the design.
Design Files: Photoshop (PSD) files for our printing specifications will be supplied.

Card Size & Material:
Dimensions: 3.5" x 2"
Material: 1/8" Radius Plastic Business Cards with 1/8" Rounded Corners
Clear plastic background—the design should strategically incorporate transparency.
Orientation: The card should be designed in landscape format for a sleek and professional presentation.

Design Requirements:
Logo Prominence
The logo must be the focal point of the card.
Space should be used effectively to draw attention to the logo while maintaining a minimalist layout.

Clear Plastic Integration
The transparent background should create the illusion of blank space, enhancing the modern and high-quality feel.
Avoid any frosted effects—we do not want white areas to appear semi-transparent.

Minimalist & Impactful
Clean, structured, and easy to read at a glance.
Focus on sharp contrast to ensure legibility and visibility.
The design should instill confidence and reflect our role as a leading plastics manufacturer.

Color Palette & Contrast
Primary Colors: Blue, Black, White, and Grey
Use bold black or blue for text and key elements to ensure they stand out against the clear plastic.
Avoid light, pastel, or neon colors that may fade into the plastic background.
No frosted or semi-transparent white—we do not want a cloudy effect.

Typography & Information Hierarchy
Bold, modern typography—clear, professional, and highly legible.
The business card should highlight:
Company Logo (Primary Focus)
Full Name & Title
Phone Number
Email
Website

Brand Representation
The card should reflect our expertise in manufacturing high-quality custom plastics for large-scale packaging and distribution businesses.
Our clients rely on us to enhance their brand presence through custom plastic solutions, and our business cards should reinforce that sense of precision and trust.

Final Considerations
Utilize the clear plastic effectively to differentiate our brand from standard business cards.
Maintain a sleek, professional aesthetic while ensuring all text and elements remain legible.
The design should align with our industry, conveying reliability and innovation.
We look forward to seeing a design that captures our brand identity, maximizes the clear plastic medium, and makes a strong, professional impact on our clients.

```html
<!DOCTYPE html>
<html lang="en">
<head>
<meta charset="utf-8">
<title>Lumvex Crating Business Card</title>
<link href="https://fonts.googleapis.com/css2?family=Montserrat:wght@400;500;600;700&display=swap" rel="stylesheet">
<style>
  :root {
    --page-bg: #e4e2de;
    --card-clear: #f1f2f1;
    --card-edge: #d3d6d6;
    --ink: #2a2a2a;
    --ink-soft: #3a3a3a;
    --teal: #17798a;
  }
  * { box-sizing: border-box; margin: 0; padding: 0; }
  html, body {
    width: 1200px; height: 1047px; overflow: hidden;
    background: var(--page-bg);
    font-family: "Montserrat", Arial, sans-serif;
  }
  .card {
    position: absolute; left: 126px; top: 265px;
    width: 948px; height: 518px;
    background: var(--card-clear);
    border: 1px solid var(--card-edge);
    border-radius: 22px;
    overflow: hidden;
  }
  .brand {
    position: absolute; left: 44px; top: 62px;
    display: flex; align-items: center; gap: 16px;
  }
  .brand-square { width: 46px; height: 46px; background: var(--teal); }
  .brand-name {
    font-weight: 600; font-size: 44px; letter-spacing: 0.5px;
    color: var(--ink); line-height: 1;
  }
  .name-bar {
    position: absolute; left: 4px; top: 200px;
    width: 14px; height: 72px; background: var(--teal);
  }
  .person-name {
    position: absolute; left: 40px; top: 196px;
    font-weight: 700; font-size: 40px; letter-spacing: 0.5px;
    color: var(--teal); line-height: 1;
  }
  .person-title {
    position: absolute; left: 40px; top: 244px;
    font-weight: 500; font-size: 23px; color: var(--ink-soft);
  }
  .address {
    position: absolute; left: 38px; top: 300px;
    font-weight: 500; font-size: 24px; line-height: 38px; color: var(--ink-soft);
  }
  .contacts {
    position: absolute; left: 38px; top: 388px;
    list-style: none; font-weight: 500; font-size: 23px; color: var(--ink-soft);
  }
  .contacts li { display: flex; align-items: center; gap: 10px; height: 37px; }
  .contacts svg { width: 22px; height: 22px; fill: var(--ink-soft); }
  .accent-square {
    position: absolute; left: 520px; top: 80px;
    width: 360px; height: 360px;
    border: 34px solid var(--teal);
  }
</style>
</head>
<body>
  <div class="card">
    <div class="brand">
      <div class="brand-square"></div>
      <div class="brand-name">Lumvex Crating</div>
    </div>

    <div class="name-bar"></div>
    <div class="person-name">DANIEL HART</div>
    <div class="person-title">Managing Director</div>

    <div class="address">Your address, City<br>State, Zip 1234</div>

    <ul class="contacts">
      <li>
        <svg viewBox="0 0 24 24" aria-hidden="true"><path d="M3 8c0-2 4-4 9-4s9 2 9 4v2h-5V8H8v2H3z M6 11h12l2 8H4z M12 13a2.5 2.5 0 1 0 0 5a2.5 2.5 0 0 0 0-5z"/></svg>
        123 456 789
      </li>
      <li>
        <svg viewBox="0 0 24 24" aria-hidden="true"><path d="M2 6h20v2l-10 6L2 8z M2 10l10 6l10-6v9H2z"/></svg>
        info@youremail.com
      </li>
      <li>
        <svg viewBox="0 0 24 24" aria-hidden="true"><circle cx="12" cy="12" r="10"/><path d="M8 7c2 0 3 2 2 3s-3 1-3 3s2 2 2 4M15 5c0 2 2 2 3 3M16 14c1 1 0 3-1 4" stroke="#f1f2f1" stroke-width="1.6" fill="none"/></svg>
        www.yourwebsite.com
      </li>
    </ul>

    <div class="accent-square"></div>
  </div>
</body>
</html>
```